Tarn - Stationary Design/Layout

We are a well established clothing design and manufacturing company (Tarn Sourcing) based in London UK, with our own factory in Bangladesh, supplying to many fashion retailers and brands. Our factory has very high environmental and ethical standards with people at its heart. Our quality of garments are second to none.
Our new logo has been proudly developed by the Pixel Guild community last month, we are now in the second phase and need the layout designed for our letterheads, double sided business cards, compliment slip and clothing ticket. Feel as creative as you like, but make sure it looks great!!
***The Logo - the logo design and colour is set and should NOT be changed and stay on a dark grey backround. The logo artwork to use is attached.
***Details to use for the business card:
Dorian Pelham
Direct Line: 020 7946 0158
dorian@tarnsourcing-example.com
Tarn Sourcing Ltd.
57 - 59 Hollin Row
Wrenfield . Ashby
NW9 4QT
Switchboard: 020 7946 0274
Fax: 020 7946 0274
www.tarnsourcing-example.co.uk
***Details to use for the letterhead and compliment slip:
Tarn Sourcing Ltd.
57 - 59 Hollin Row
Wrenfield . Ashby
NW9 4QT
Fax: 020 7946 0274
www.tarnsourcing-example.co.uk
***Details for Swing Ticket:
Size: 12cm height by 5.5cm width
One side need to have just the logo without the 'Sourcing', on the other it needs to stay blank

```html
<!DOCTYPE html>
<html lang="en">
<head>
<meta charset="utf-8">
<title>Tarn Sourcing – Stationary #1</title>
<link rel="stylesheet" href="https://fonts.googleapis.com/css2?family=Source+Sans+3:ital,wght@0,400;0,600;1,400&display=swap">
<style>
  :root{
    --bg-top:#f4f4f4;
    --bg-bottom:#d9d9d9;
    --brand-grey:#6d6e70;
    --brand-grey-dark:#5e5f61;
    --wave-light:#b9babc;
    --brand-cyan:#a6dde1;
    --paper:#ffffff;
    --card-tint:#f5fbfc;
    --label:#6a6a6a;
    --ink:#4a4a4a;
    --rule:#c8c8c8;
  }
  *{box-sizing:border-box;margin:0;padding:0}
  html,body{width:1200px;height:900px;overflow:hidden}
  body{
    position:relative;
    font-family:"Source Sans 3",sans-serif;
    background:linear-gradient(180deg,var(--bg-top) 0%,var(--bg-bottom) 72%,#e6e6e6 73%,#efefef 100%);
  }
  .label{position:absolute;color:var(--label);font-size:17px;letter-spacing:.2px}
  .shadow{box-shadow:0 6px 18px rgba(0,0,0,.22)}
  .wordmark{font-family:"Source Sans 3",sans-serif;font-weight:600;color:var(--brand-cyan);letter-spacing:1px;line-height:1;white-space:nowrap}

  /* Letterhead */
  .letterhead{position:absolute;left:75px;top:92px;width:468px;height:645px;background:var(--paper)}
  .sheet-header{position:absolute;left:0;top:0;width:100%;height:120px}
  .sheet-address{position:absolute;color:#fff;font-size:6.5px;line-height:8.4px;white-space:nowrap}
  .letterhead .sheet-address{left:343px;top:8px}
  .letterhead .wordmark{position:absolute;left:25px;top:46px;font-size:15px}

  /* Business cards */
  .card{position:absolute;left:512px;width:252px;height:143px;border-radius:12px;overflow:hidden}
  .card-front{top:175px;background:var(--card-tint)}
  .card-tab{position:absolute;left:0;top:45px;width:120px;height:63px;background:var(--brand-grey-dark);border-radius:0 32px 32px 0}
  .card-tab .wordmark{position:absolute;left:10px;top:24px;font-size:13px}
  .card-details{position:absolute;left:138px;top:14px;width:108px;color:var(--ink);font-size:6.6px;line-height:8.2px;white-space:nowrap}
  .card-name{font-size:11.5px;font-weight:600;line-height:14px;margin-bottom:4px}
  .card-details b{font-weight:600}
  .card-rule{border-top:1px solid var(--rule);margin:4px 0 5px}
  .card-back{top:331px;height:141px}
  .pattern{position:absolute;inset:0;background:linear-gradient(135deg,#727375,#67686a)}
  .card-back .wordmark{position:absolute;left:139px;top:57px;font-size:24px}

  /* Side panel */
  .brand-panel{position:absolute;left:879px;top:0;width:252px;height:349px;background:var(--brand-grey);border-radius:0 0 10px 10px}
  .panel-title{position:absolute;right:17px;top:200px;color:#fff;font-size:18px}
  .panel-rule{position:absolute;left:16px;right:17px;top:238px;border-top:1px solid #c9cacb}
  .brand-panel .wordmark{position:absolute;right:17px;top:268px;font-size:33px}

  /* Compliment slip */
  .slip{position:absolute;left:30px;top:552px;width:502px;height:272px;background:var(--paper);transform:rotate(-1.3deg)}
  .slip .sheet-header{height:112px}
  .slip .sheet-address{left:352px;top:20px}
  .slip .wordmark{position:absolute;left:28px;top:64px;font-size:15px}
  .slip-compliments{position:absolute;right:30px;bottom:28px;font-style:italic;font-size:12px;color:var(--ink)}

  /* Swing ticket */
  .ticket{position:absolute;left:573px;top:588px;width:335px;height:152px;border-radius:12px;overflow:hidden;transform:rotate(-2deg)}
  .ticket-hole{position:absolute;left:28px;top:86px;width:20px;height:20px;border-radius:50%;background:#e4e4e4}
  .ticket .wordmark{position:absolute;left:226px;top:62px;font-size:25px}
</style>
</head>
<body>

  <div class="label" style="left:20px;top:72px">Letterhead</div>
  <section class="letterhead shadow">
    <svg class="sheet-header" viewBox="0 0 468 120" preserveAspectRatio="none" aria-hidden="true">
      <path d="M0 0H468V66C390 60 330 100 220 92C130 84 60 88 0 104Z" fill="var(--wave-light)"/>
      <path d="M0 0H468V58C390 52 330 92 220 84C130 76 60 78 0 92Z" fill="var(--brand-grey)"/>
    </svg>
    <div class="sheet-address">Tarn Sourcing Ltd.<br>57 - 59 Hollin Row<br>Wrenfield . Ashby<br>NW9 4QT<br>Switchboard: 020 7946 0274<br>Fax: 020 7946 0274</div>
    <div class="wordmark">Tarn Sourcing</div>
  </section>

  <div class="label" style="left:691px;top:147px">Business Card (Front)</div>
  <section class="card card-front shadow">
    <div class="card-tab"><div class="wordmark">Tarn Sourcing</div></div>
    <div class="card-details">
      <div class="card-name">Dorian Pelham</div>
      <div><b>Direct Line:</b> 020 7946 0158</div>
      <div>dorian@tarnsourcing-example.com</div>
      <div class="card-rule"></div>
      <div>Tarn Sourcing Ltd.</div>
      <div>57 - 59 Hollin Row</div>
      <div>Wrenfield . Ashby</div>
      <div>NW9 4QT</div>
      <div><b>Switchboard:</b> 020 7946 0274</div>
      <div><b>Fax:</b> 020 7946 0274</div>
      <div>www.tarnsourcing-example.co.uk</div>
    </div>
  </section>

  <section class="card card-back shadow">
    <div class="pattern" role="img" aria-label="Repeating brand name pattern in grey"></div>
    <div class="wordmark">Tarn</div>
  </section>
  <div class="label" style="left:691px;top:482px">Business Card (Back)</div>

  <aside class="brand-panel">
    <div class="panel-title">Stationary #1</div>
    <div class="panel-rule"></div>
    <div class="wordmark">Tarn Sourcing</div>
  </aside>

  <section class="slip shadow">
    <svg class="sheet-header" viewBox="0 0 502 112" preserveAspectRatio="none" aria-hidden="true">
      <path d="M0 0H502V90C420 84 350 108 235 102C140 96 60 96 0 110Z" fill="var(--wave-light)"/>
      <path d="M0 0H502V82C420 76 350 100 235 94C140 88 60 86 0 98Z" fill="var(--brand-grey)"/>
    </svg>
    <div class="sheet-address">Tarn Sourcing Ltd.<br>57 - 59 Hollin Row<br>Wrenfield . Ashby<br>NW9 4QT<br>Switchboard: 020 7946 0274<br>Fax: 020 7946 0274</div>
    <div class="wordmark">Tarn Sourcing</div>
    <div class="slip-compliments">With Compliments.</div>
  </section>
  <div class="label" style="left:86px;top:830px">Compliment Slip</div>

  <section class="ticket shadow">
    <div class="pattern" role="img" aria-label="Repeating brand name pattern in grey"></div>
    <div class="ticket-hole"></div>
    <div class="wordmark">Tarn</div>
  </section>
  <div class="label" style="left:829px;top:758px">Swing Ticket</div>

</body>
</html>
```